Business Card Design for a coaching and consulting company (usage of existing logo)

We need a business card design for a new business start up (coaching & consulting) incorporating an existing logo that has just been created by a tallomira designer.

The business card should pick up the existing logo and its colours (please check out variations as well) and look fresh, light, open and professional. The business card must be applicable for worldwide clients and must adhere to the standard Australian business card measurements. We are open for fun designs that require special print techniques as long as it doesn't get too expensive/fancy in the print process. We prefer versions that use both sides of the business card as we personally find 1-siders a little bit boring.

Business

```html
<!DOCTYPE html>
<html lang="en">
<head>
<meta charset="utf-8">
<title>Harborline Business Card</title>
<link rel="stylesheet" href="https://fonts.googleapis.com/css2?family=Open+Sans:wght@400;600;700&display=swap">
<style>
  :root {
    --stage: #4a2e1c;
    --card-white: #ffffff;
    --brand-yellow: #f5c623;
    --ink: #2f2f2f;
    --ink-soft: #1c1c1c;
    --divider: #3a3a3a;
  }
  * { box-sizing: border-box; margin: 0; padding: 0; }
  html, body {
    width: 1200px; height: 463px; overflow: hidden;
    background: var(--stage);
    font-family: "Open Sans", Arial, sans-serif;
  }
  .stage {
    position: relative; width: 1200px; height: 463px;
    display: flex; align-items: center; justify-content: center; gap: 60px;
  }
  .card {
    position: relative; width: 540px; height: 310px;
    border-radius: 18px; overflow: hidden;
    background: var(--card-white);
    box-shadow: 0 6px 14px rgba(0,0,0,0.45);
  }

  /* Back side: brand + contact */
  .card--contact { display: flex; }
  .contact-brand {
    width: 232px; display: flex; flex-direction: column;
    justify-content: center; align-items: center; gap: 6px;
  }
  .contact-divider { width: 5px; background: var(--divider); }
  .contact-panel {
    flex: 1; background: var(--brand-yellow);
    padding: 48px 26px 0 30px; color: var(--ink-soft);
  }
  .person-name { font-size: 18px; font-weight: 700; line-height: 1.2; }
  .person-role { font-size: 14px; margin-top: 4px; }
  .contact-list { list-style: none; margin-top: 20px; font-size: 13px; line-height: 1.55; }
  .contact-list li { display: flex; align-items: center; gap: 6px; }
  .contact-list svg { width: 11px; height: 11px; flex: none; }
  .postal { margin-top: 20px; font-size: 13px; line-height: 1.5; font-style: normal; }

  /* Shared brand lockup */
  .brand-lockup { display: flex; align-items: center; gap: 10px; }
  .brand-dot {
    border-radius: 50%; background: var(--brand-yellow); flex: none;
  }
  .brand-name { font-weight: 600; color: var(--ink); letter-spacing: -0.5px; }
  .brand-tagline { color: var(--brand-yellow); font-weight: 400; }

  .card--contact .brand-dot { width: 16px; height: 16px; }
  .card--contact .brand-name { font-size: 28px; }
  .card--contact .brand-tagline { font-size: 14px; }

  /* Front side: brand */
  .card--brand {
    display: flex; flex-direction: column; align-items: center; justify-content: center;
  }
  .card--brand .brand-dot { width: 26px; height: 26px; }
  .card--brand .brand-name { font-size: 50px; }
  .card--brand .brand-tagline { font-size: 22px; margin-top: 4px; }
  .card--brand .site {
    position: absolute; bottom: 38px; left: 0; right: 0; text-align: center;
    font-size: 15px; letter-spacing: 2px; color: var(--ink-soft);
  }
</style>
</head>
<body>
<main class="stage">

  <section class="card card--contact" aria-label="Business card, contact side">
    <div class="contact-brand">
      <div class="brand-lockup">
        <span class="brand-dot"></span>
        <span class="brand-name">Harborline</span>
      </div>
      <span class="brand-tagline">Coaching &amp; Consulting</span>
    </div>
    <div class="contact-divider"></div>
    <div class="contact-panel">
      <p class="person-name">Mareike Lindqvist</p>
      <p class="person-role">Owner</p>
      <ul class="contact-list">
        <li>
          <svg viewBox="0 0 12 12" aria-hidden="true"><circle cx="6" cy="6" r="5.4" fill="none" stroke="currentColor" stroke-width="1.2"/><path d="M4 3.2l1 1.4-.6.7a4 4 0 0 0 2.3 2.3l.7-.6 1.4 1-.6 1C6 8.8 3.2 6 3 4z" fill="currentColor"/></svg>
          555-210-4836
        </li>
        <li>
          <svg viewBox="0 0 12 12" aria-hidden="true"><rect x="0.8" y="2.5" width="10.4" height="7" rx="1" fill="currentColor"/><path d="M1.2 3l4.8 3.4L10.8 3" fill="none" stroke="#f5c623" stroke-width="1"/></svg>
          mareike@harborline.com
        </li>
        <li>
          <svg viewBox="0 0 12 12" aria-hidden="true"><g fill="none" stroke="currentColor" stroke-width="1"><circle cx="6" cy="6" r="5"/><ellipse cx="6" cy="6" rx="2.2" ry="5"/><path d="M1 6h10M1.8 3.5h8.4M1.8 8.5h8.4"/></g></svg>
          www.harborline.com
        </li>
      </ul>
      <address class="postal">Street Name, City Name<br>State Zipcode</address>
    </div>
  </section>

  <section class="card card--brand" aria-label="Business card, brand side">
    <div class="brand-lockup">
      <span class="brand-dot"></span>
      <span class="brand-name">Harborline</span>
    </div>
    <span class="brand-tagline">Coaching &amp; Consulting</span>
    <p class="site">www.harborline.com</p>
  </section>

</main>
</body>
</html>
```